Business cards to launch an education platform

Hi,
I am looking at having new business cards designed.
I am a startup, developing a web platform for schools and university, the education world. It's an online assessment system.
I would like a card that looks classy, and that is using the colors and the font of my logo.

I have attached:
1) my logo
2) A business card that I have designed quickly so you can have all the information required in the card, but I really don't like it.
3) The font that I am using (Lato Regular) to design my web platform
4) Some screenshots of my web platform so you can have a look at the style that I have.

Target Market(s)

Major market: Education system: Schools and university
Minor markets: Business in general

Industry/Entity Type

Business

Contact Information for Business Card

Lydia Marsh
Director

M: 0437 681 902
E: lydia.marsh@copperLeafSystems.com.au

Requirements
Must have
• The colors of my logo

```html
<!DOCTYPE html>
<html lang="en">
<head>
<meta charset="utf-8">
<title>Copper Leaf Systems – Business Card</title>
<link rel="stylesheet" href="https://fonts.googleapis.com/css2?family=Lato:wght@400&display=swap">
<style>
  :root {
    --stage-top: #222222;
    --stage-bottom: #050505;
    --card-white: #ffffff;
    --navy: #14386b;
    --sky: #1fa0dc;
    --back-top: #23a4e0;
    --back-bottom: #1470bb;
    --mark-back: #1c84c9;
  }
  * { box-sizing: border-box; margin: 0; padding: 0; }
  html, body { width: 1200px; height: 900px; overflow: hidden; }
  body {
    position: relative;
    background: linear-gradient(180deg, var(--stage-top) 0%, var(--stage-bottom) 100%);
    font-family: "Lato", Arial, sans-serif;
  }
  .card {
    position: absolute;
    top: 306px;
    width: 440px;
    height: 271px;
    border-radius: 11px;
    overflow: hidden;
  }
  .card-front { left: 149px; background: var(--card-white); }
  .card-back {
    left: 608px;
    background: linear-gradient(180deg, var(--back-top) 0%, var(--back-bottom) 100%);
  }
  .holder-name {
    position: absolute; left: 24px; top: 24px;
    font-size: 18px; color: var(--sky); line-height: 1;
  }
  .holder-role {
    position: absolute; left: 24px; top: 49px;
    font-size: 13px; color: var(--navy); line-height: 1;
  }
  .brand {
    position: absolute; right: 26px; top: 86px;
    display: flex; align-items: center; gap: 13px;
  }
  .brand-name {
    text-align: right; color: var(--navy);
    font-size: 22px; letter-spacing: 2px; line-height: 1.12;
    text-transform: uppercase;
  }
  .brand-divider { width: 1.5px; height: 80px; background: var(--sky); }
  .brand-square { width: 58px; height: 58px; background: var(--navy); }
  .contact {
    position: absolute; left: 24px; top: 201px;
    list-style: none; color: var(--navy); font-size: 13px; line-height: 16px;
  }
  .contact li { display: flex; align-items: center; gap: 6px; }
  .contact svg { width: 10px; height: 10px; fill: var(--sky); flex: none; }
  .back-square {
    position: absolute; left: 170px; top: 86px;
    width: 100px; height: 100px;
    background: var(--mark-back);
    box-shadow: inset 1px 1px 0 rgba(255,255,255,0.25), inset -1px -1px 0 rgba(0,0,0,0.15);
  }
</style>
</head>
<body>
  <section class="card card-front" aria-label="Business card front">
    <p class="holder-name">Lydia Marsh</p>
    <p class="holder-role">Director</p>

    <div class="brand">
      <p class="brand-name">Copper Leaf<br>Systems</p>
      <span class="brand-divider"></span>
      <span class="brand-square"></span>
    </div>

    <ul class="contact">
      <li>
        <svg viewBox="0 0 10 10" aria-hidden="true"><path d="M2 0.5 L3.6 0.5 L4.2 2.8 L3 3.7 C3.6 5 4.9 6.4 6.3 7 L7.2 5.8 L9.5 6.4 L9.5 8 C9.5 8.9 8.8 9.5 8 9.5 C4 9.2 0.8 6 0.5 2 C0.5 1.2 1.1 0.5 2 0.5 Z"/></svg>
        <span>0437 681 902</span>
      </li>
      <li>
        <svg viewBox="0 0 10 10" aria-hidden="true"><path d="M0.5 2 L9.5 2 L9.5 8.5 L0.5 8.5 Z M1.2 2.6 L5 5.6 L8.8 2.6 Z" fill-rule="evenodd"/></svg>
        <span>lydia.marsh@copperLeafSystems.com.au</span>
      </li>
    </ul>
  </section>

  <section class="card card-back" aria-label="Business card back">
    <span class="back-square"></span>
  </section>
</body>
</html>
```